Modern Business Card for Larkwell 2018

Our company assumes the best about people. We are creating an online community of entrepreneurs and business leaders who struggle with marketing their business online.

This business card should POP! We recently got a new logo and are launching a new website next month, so our business cards should make a statement that feels:
-Fresh
-Smart
-Trustworthy
-Fun

Target Market(s)

small business owners, entrepreneurs

Industry/Entity Type

Digital Marketing

Contact Information for Business Card

Dimensions: 3.5" x 2"

Font styles to use
Sans Serif

Colors
f37122
ffffff

Requirements
Must have
• We need a business card with a modern, bold design. We will use one side of the card as a lead-generation offer, so text on one side will need to fit up to 140 characters. The business card should stick to our core colors (orange, black, and white).
Nice to have
• We think a vertical "portrait" design could be interesting.
Should not have
• Should not look like a traditional business card. The round icon should stand out from a distance.

```html
<!DOCTYPE html>
<html lang="en">
<head>
<meta charset="utf-8">
<title>Larkwell Business Card</title>
<link rel="stylesheet" href="https://fonts.googleapis.com/css2?family=Montserrat:wght@400;500;600;700;800&display=swap">
<style>
  :root {
    --orange: #f37122;
    --orange-deep: #ee6224;
    --orange-soft: #f58a2a;
    --ink: #222222;
    --band-dark: #333235;
    --white: #ffffff;
    --mist: #f3f3f3;
    --stage: #d9d9d9;
  }
  * { box-sizing: border-box; margin: 0; padding: 0; }
  html, body { width: 1200px; height: 1200px; overflow: hidden; }
  body {
    background: var(--stage);
    font-family: "Montserrat", Arial, sans-serif;
    position: relative;
  }
  .card-set {
    position: absolute;
    left: 200px; top: 250px;
    width: 800px; height: 700px;
    display: flex;
  }
  .card { width: 400px; height: 700px; position: relative; overflow: hidden; }

  /* Offer side */
  .card--offer { background: var(--orange-deep); color: var(--white); }
  .offer__glow {
    position: absolute; left: -150px; top: 130px;
    width: 520px; height: 520px; border-radius: 50%;
    background: radial-gradient(circle, rgba(245,138,42,0.55), rgba(245,138,42,0) 70%);
  }
  .brand {
    position: absolute; top: 38px; left: 0; right: 0;
    display: flex; align-items: center; justify-content: center; gap: 10px;
    font-weight: 800; font-size: 34px; letter-spacing: 1px; text-transform: uppercase;
  }
  .brand__dot { width: 28px; height: 28px; border-radius: 50%; background: var(--white); }
  .offer__headline {
    position: absolute; top: 292px; left: 0; right: 0;
    text-align: center; font-weight: 700; font-size: 21px;
    line-height: 34px; letter-spacing: 2px; text-transform: uppercase;
  }
  .offer__band {
    position: absolute; top: 546px; left: 0; right: 0; height: 112px;
    background: var(--band-dark);
    display: flex; flex-direction: column; align-items: center; justify-content: center;
    text-align: center; font-size: 14.5px; line-height: 20px; font-weight: 500;
  }
  .offer__url { color: var(--orange); font-weight: 600; font-size: 18px; margin-top: 4px; }

  /* Contact side */
  .card--contact { background: var(--white); color: var(--ink); }
  .contact__sweep {
    position: absolute; left: -60px; top: 420px;
    width: 640px; height: 160px; background: var(--mist);
    transform: rotate(38deg); transform-origin: left top;
  }
  .contact__mark {
    position: absolute; top: 68px; left: 50%; transform: translateX(-50%);
    display: flex; align-items: center; gap: 8px;
    font-weight: 800; font-size: 15px; letter-spacing: 1px; text-transform: uppercase; color: var(--orange);
  }
  .contact__mark-dot { width: 40px; height: 40px; border-radius: 50%; background: var(--orange); }
  .contact__role {
    position: absolute; top: 210px; left: 0; right: 0; text-align: center;
    font-weight: 700; font-size: 13.5px; letter-spacing: 0.3px; text-transform: uppercase;
  }
  .contact__name {
    position: absolute; top: 250px; left: 40px; width: 320px; height: 200px;
    background: linear-gradient(135deg, rgba(243,113,34,0.85) 0%, rgba(243,113,34,0.5) 45%, rgba(34,34,34,0.75) 100%);
    border-radius: 6px;
  }
  .contact__band {
    position: absolute; top: 580px; left: 0; right: 0; height: 56px;
    background: var(--orange); color: var(--white);
    display: flex; align-items: center; justify-content: center;
    font-weight: 700; font-size: 14px; letter-spacing: 0.3px; text-transform: uppercase;
  }
</style>
</head>
<body>
  <main class="card-set">
    <section class="card card--offer">
      <div class="offer__glow"></div>
      <div class="brand"><span class="brand__dot"></span><span>Larkwell</span></div>
      <p class="offer__headline">Reach more people.<br>Make more money.<br>Create more impact.</p>
      <div class="offer__band">
        <span>Get Your Free Larkwell Starter Package</span>
        <span>and Our Marketing Guide Today at</span>
        <span class="offer__url">larkwellhub.com/start</span>
      </div>
    </section>
    <section class="card card--contact">
      <div class="contact__sweep"></div>
      <div class="contact__mark"><span class="contact__mark-dot"></span></div>
      <p class="contact__role">Story Marketing Coach</p>
      <div class="contact__name" role="img" aria-label="Hand-lettered signature name: Dana Whitfield, in orange and black brush script"></div>
      <div class="contact__band">dana@larkwellhub.com</div>
    </section>
  </main>
</body>
</html>
```